A land page lead collector for people who want to reduce there postage costs

We are looking to create a single page website landing page to collect leads of people who want to reduce there postage costs.

The form should basically ask:

Name:
Business Name:
Address:
Town:
Post Code:
Email:
Phone:
Letter Volume Per Week:
Parcel Volume Per Week:

We should basically be advertising cheaper postage costs.

We will not be showing prices on this website we will just be collecting the leads.

Our competition website is as follows https://mailfernquest.com

But we are not a online service. This is just a collector to get leads of people who want to save money on there postage costs.
Updates

Target Market(s)

Small and medium sized enterprises

Industry/Entity Type

Advertising

Number of Pages Required

1 page

Colors
ec2027
0356a4

Requirements
Must have
• Form above the fold of the page
Nice to have
• Colour red and blue.
• Parallax design would be nice.

```html
<!DOCTYPE html>
<html lang="en">
<head>
<meta charset="utf-8">
<title>Stamp Saver – Cut Your Postage Costs</title>
<link href="https://fonts.googleapis.com/css2?family=Open+Sans:wght@400;600&family=PT+Sans:wght@400;700&family=Courgette&display=swap" rel="stylesheet">
<style>
  :root {
    --brand-red: #ec2027;
    --brand-red-dark: #c8141a;
    --brand-blue: #0356a4;
    --ink: #2b2b2b;
    --muted: #8a8a8a;
    --white: #ffffff;
    --footer-bg: #252525;
    --panel-bg: rgba(40, 40, 40, 0.72);
    --panel-base: #555555;
    --field-text: #7d8fb0;
  }
  * { box-sizing: border-box; margin: 0; padding: 0; }
  html, body { width: 1072px; height: 1200px; overflow: hidden; background: var(--white); }
  body { font-family: "PT Sans", sans-serif; color: var(--ink); }
  .page { position: relative; width: 1072px; height: 1200px; overflow: hidden; }

  /* Hero */
  .hero {
    position: absolute; left: 0; top: 0; width: 1072px; height: 611px;
    background:
      radial-gradient(ellipse at 30% 30%, rgba(180, 60, 60, 0.6), transparent 60%),
      radial-gradient(ellipse at 85% 50%, #b0121a, transparent 55%),
      linear-gradient(120deg, #6a1a1e 0%, #a01820 35%, #5a2a2c 55%, #9c0f16 80%, #7a0c12 100%);
  }
  .site-header { position: absolute; left: 54px; top: 23px; right: 53px; height: 30px; display: flex; align-items: center; }
  .brand { font-family: "Open Sans", sans-serif; font-size: 21px; font-weight: 400; color: var(--white); letter-spacing: 0.2px; }
  .main-nav { position: absolute; left: 333px; top: 0; height: 30px; display: flex; align-items: center; }
  .main-nav a { position: absolute; white-space: nowrap; color: var(--white); text-decoration: none; font-family: "PT Sans", sans-serif; font-size: 14px; }
  .login-btn {
    position: absolute; left: 886px; top: 0; width: 79px; height: 29px;
    border: 1px solid var(--white); color: var(--white); font-size: 13px;
    display: flex; align-items: center; justify-content: center; gap: 6px;
  }
  .hero-title {
    position: absolute; left: 0; width: 1072px; top: 205px; text-align: center;
    font-family: "Open Sans", sans-serif; font-size: 27px; color: var(--white); letter-spacing: 0.3px;
  }
  .slider-arrow { position: absolute; top: 292px; color: rgba(255,255,255,0.55); font-size: 26px; }
  .slider-arrow.prev { left: 54px; }
  .slider-arrow.next { left: 1003px; }

  /* Lead form panel */
  .lead-panel {
    position: absolute; left: 264px; top: 318px; width: 547px; height: 323px;
    border: 2px solid var(--white); border-bottom: none;
    background: linear-gradient(to bottom, var(--panel-bg) 0%, var(--panel-bg) 90%, var(--panel-base) 90%);
    box-shadow: 0 14px 18px -10px rgba(0,0,0,0.25);
  }
  .stamp {
    position: absolute; left: 250px; top: 302px; width: 52px; height: 52px;
    transform: rotate(40deg); background: #9a6f1e; border: 4px solid #f2ece0;
  }
  .lead-title {
    position: absolute; left: 0; width: 100%; top: 14px; text-align: center;
    font-family: "Courgette", cursive; font-size: 26px; color: var(--white);
  }
  .field {
    position: absolute; width: 165px; height: 27px; background: var(--white);
    border: 1px solid #d9d9d9; border-radius: 2px; padding-left: 23px;
    font-family: "Courgette", cursive; font-size: 11px; color: var(--field-text);
    display: flex; align-items: center;
  }
  .field.select .caret {
    position: absolute; right: 0; top: 0; width: 24px; height: 25px;
    border-left: 1px solid #d9d9d9; display: flex; align-items: center; justify-content: center;
  }
  .submit-btn {
    position: absolute; left: 305px; top: 261px; width: 97px; height: 27px;
    background: var(--brand-red); color: var(--white); border-radius: 3px;
    font-family: "Open Sans", sans-serif; font-size: 15px;
    display: flex; align-items: center; justify-content: center;
  }

  /* Welcome */
  .welcome-title { position: absolute; left: 0; width: 1072px; top: 674px; text-align: center; font-family: "Open Sans", sans-serif; font-size: 20px; color: var(--ink); }
  .welcome-text { position: absolute; left: 120px; width: 832px; top: 706px; text-align: center; font-size: 12.5px; line-height: 25px; color: var(--muted); }

  /* Features */
  .feature-icon { position: absolute; width: 74px; height: 72px; border-radius: 8px; }
  .feature-text { position: absolute; width: 200px; font-size: 14px; line-height: 25px; color: var(--brand-blue); }

  .learn-more {
    position: absolute; left: 439px; top: 1020px; width: 195px; height: 36px;
    background: linear-gradient(to bottom, var(--brand-red), var(--brand-red-dark));
    border: 1px solid #a01016; border-radius: 2px; color: var(--white);
    font-family: "Open Sans", sans-serif; font-size: 16px;
    display: flex; align-items: center; justify-content: center;
  }

  /* Footer */
  .site-footer { position: absolute; left: 0; top: 1086px; width: 1072px; height: 114px; background: var(--footer-bg); }
  .footer-copy { position: absolute; left: 54px; top: 38px; font-size: 10.5px; color: #d8d8d8; }
  .footer-terms { position: absolute; left: 54px; top: 63px; font-size: 10.5px; color: #d8d8d8; }
  .social { position: absolute; left: 941px; top: 47px; display: flex; gap: 7px; }
  .social span { width: 21px; height: 21px; background: var(--white); border-radius: 3px; }
</style>
</head>
<body>
<div class="page">

  <section class="hero" role="img" aria-label="Photo of a father and child posting a letter into a red post box">
    <header class="site-header">
      <div class="brand">STAMP SAVER</div>
      <nav class="main-nav">
        <a style="left:0">Home</a>
        <a style="left:83px">About Us</a>
        <a style="left:186px">Features</a>
        <a style="left:285px">Services</a>
        <a style="left:380px">Tracking</a>
        <a style="left:478px">Contact</a>
      </nav>
      <div class="login-btn">
        <svg width="10" height="11" viewBox="0 0 10 11"><circle cx="5" cy="3" r="2.6" fill="#fff"/><path d="M0 11 C0 6.5 10 6.5 10 11 Z" fill="#fff"/></svg>
        Login
      </div>
    </header>
    <h1 class="hero-title">LOREM IPSUM DOLOR SIT AMET CONSECTETUR ADIPISCING</h1>
    <span class="slider-arrow prev">&#10094;</span>
    <span class="slider-arrow next">&#10095;</span>
  </section>

  <form class="lead-panel">
    <div class="lead-title">Call To Action</div>
    <div class="field" style="left:72px;top:64px">Name.....</div>
    <div class="field" style="left:304px;top:64px">Business Name.....</div>
    <div class="field" style="left:72px;top:113px">Address.....</div>
    <div class="field select" style="left:304px;top:113px">Town.....
      <span class="caret"><svg width="9" height="6" viewBox="0 0 9 6"><path d="M1 1 L4.5 4.5 L8 1" stroke="#222" stroke-width="1.8" fill="none"/></svg></span>
    </div>
    <div class="field" style="left:72px;top:163px">Post Code.....</div>
    <div class="field" style="left:304px;top:163px">Email....</div>
    <div class="field" style="left:72px;top:212px">Phone....</div>
    <div class="field" style="left:304px;top:212px">Letter Volume Per Week...</div>
    <div class="field" style="left:72px;top:260px;padding-left:20px">Parcel Volume Per Week...</div>
    <div class="submit-btn">SUBMIT</div>
  </form>
  <div class="stamp" role="img" aria-label="Postage stamp illustration"></div>

  <h2 class="welcome-title">Welcome to the Stamp Saver</h2>
  <p class="welcome-text">Duis autem vel eum iriure dolor in hendrerit in vulputate velit esse molestie consequat, vel illum dolore eu feugiat nulla facilisis at vero eros et accumsan et iusto odio dignissim qui blandit praesent luptatum zzril delenit augue duis dolore te feugait nulla facilisi.</p>

  <div class="feature-icon" style="left:64px;top:784px;background:#e8dcc0" role="img" aria-label="Envelope with sticky notes icon"></div>
  <p class="feature-text" style="left:158px;top:803px">Comprehensive mail sorting facilities</p>

  <div class="feature-icon" style="left:396px;top:784px;background:#e4e4e4" role="img" aria-label="Checklist with pen icon"></div>
  <p class="feature-text" style="left:497px;top:803px">Access to DSAs, including Crown Post</p>

  <div class="feature-icon" style="left:719px;top:784px;background:#c9a273" role="img" aria-label="Stacked cardboard boxes on a pallet icon"></div>
  <p class="feature-text" style="left:818px;top:803px">The capacity to process huge volumes of mail daily</p>

  <div class="feature-icon" style="left:66px;top:893px;background:#dcdcdc" role="img" aria-label="White delivery van icon"></div>
  <p class="feature-text" style="left:160px;top:899px">Remember to fill in a customs declaration if you’re sending a parcel outside the EU</p>

  <div class="feature-icon" style="left:400px;top:893px;background:#c8c8c8" role="img" aria-label="Mailbox with letter icon"></div>
  <p class="feature-text" style="left:497px;top:899px">Include a return address on the parcel just in case your parcel can’t be delivered</p>

  <div class="feature-icon" style="left:722px;top:887px;background:#e9a441" role="img" aria-label="Open envelope with letter icon"></div>
  <p class="feature-text" style="left:819px;top:899px">Couriers may inspect your item upon collection, so it’s advised to leave the top of your box open.</p>

  <div class="learn-more">LEARN MORE</div>

  <footer class="site-footer">
    <p class="footer-copy">© Copyright 2014 Stamp Saver. All Rights Reserved.</p>
    <p class="footer-terms">Terms &amp; Conditions</p>
    <div class="social" aria-label="Social links"><span></span><span></span><span></span></div>
  </footer>
</div>
</body>
</html>
```